Business Card Design Project

New business cards that encompass our new logo.
Looking for -
Name, Title, Cell Phone, Email, Address (2 lines), Main Phone, Fax, and website.
Reason: I don't like the graphics used to show phone, fax, cell, email, web, and address.....
I like the double sided cards with logo's on the back. I do not like the logos for phone, fax, cell, address, email, or web.

```html
<!DOCTYPE html>
<html lang="en">
<head>
<meta charset="utf-8">
<title>Northpeak Kitchen Supply – Business Cards</title>
<link rel="stylesheet" href="https://fonts.googleapis.com/css2?family=Montserrat:wght@500;600;700&display=swap">
<style>
  :root {
    --page-bg: #e9e6e2;
    --card-dark: #141414;
    --card-dark-edge: #262626;
    --card-light: #ffffff;
    --brand-red: #c23a4c;
    --brand-blue: #223f8c;
    --ink-dark: #141414;
    --ink-light: #f4f4f4;
  }
  * { box-sizing: border-box; margin: 0; padding: 0; }
  html, body {
    width: 1200px;
    height: 1200px;
    overflow: hidden;
    background: var(--page-bg);
    font-family: "Montserrat", Arial, sans-serif;
  }
  .canvas {
    position: relative;
    width: 1200px;
    height: 1200px;
  }
  .card {
    position: absolute;
    width: 700px;
    height: 400px;
    border-radius: 4px;
    box-shadow: 0 14px 36px rgba(0, 0, 0, 0.22);
    overflow: hidden;
  }
  .card--dark {
    left: 110px;
    top: 150px;
    background: linear-gradient(160deg, var(--card-dark-edge) 0%, var(--card-dark) 60%);
    color: var(--ink-light);
  }
  .card--light {
    left: 390px;
    top: 640px;
    background: linear-gradient(200deg, #f1f1f1 0%, var(--card-light) 45%);
    color: var(--ink-dark);
  }
  .brand {
    position: absolute;
    left: 56px;
    display: flex;
    align-items: center;
    gap: 12px;
  }
  .brand--low { top: 200px; }
  .brand--high { top: 96px; }
  .brand__mark {
    flex: none;
    width: 18px;
    height: 18px;
    background: var(--brand-red);
  }
  .brand__name {
    width: 290px;
    font-weight: 700;
    font-size: 28px;
    line-height: 1.12;
    letter-spacing: 0.01em;
    color: var(--brand-blue);
  }
  .details {
    position: absolute;
    left: 400px;
    font-weight: 500;
    font-size: 18px;
    line-height: 1.3;
    white-space: nowrap;
  }
  .card--dark .details { top: 78px; }
  .card--light .details { top: 62px; }
  .details__name { color: var(--brand-red); }
  .details__title { color: var(--brand-blue); }
  .details__group + .details__group { margin-top: 24px; }
</style>
</head>
<body>
<main class="canvas">

  <section class="card card--dark" aria-label="Business card, dark side">
    <div class="brand brand--low">
      <span class="brand__mark"></span>
      <span class="brand__name">NORTHPEAK KITCHEN SUPPLY</span>
    </div>
    <div class="details">
      <div class="details__group">
        <p class="details__name">Evan Marlow</p>
        <p class="details__title">Owner/CEO</p>
        <p>061-738-214</p>
        <p>hello@northpeakks.com</p>
      </div>
      <div class="details__group">
        <p>482 Cedar Ridge Road</p>
        <p>Fairbrook, OR 97381</p>
        <p>Main Phone: +1 541-555-0142</p>
        <p>Fax: +1 541-555-0187</p>
      </div>
    </div>
  </section>

  <section class="card card--light" aria-label="Business card, light side">
    <div class="brand brand--high">
      <span class="brand__mark"></span>
      <span class="brand__name">NORTHPEAK KITCHEN SUPPLY</span>
    </div>
    <div class="details">
      <div class="details__group">
        <p class="details__name">Evan Marlow</p>
        <p class="details__title">Owner/CEO</p>
        <p>061-738-214</p>
        <p>hello@northpeakks.com</p>
      </div>
      <div class="details__group">
        <p>482 Cedar Ridge Road</p>
        <p>Fairbrook, OR 97381</p>
        <p>Main Phone: +1 541-555-0142</p>
        <p>Fax: +1 541-555-0187</p>
      </div>
    </div>
  </section>

</main>
</body>
</html>
```